AV GLOSSUM BUSINESS CARD DESIGN PROJECT

We need to utilize our logo that was expertly created on Sketchloom and now need to match this with a business card design.

```html
<!DOCTYPE html>
<html lang="en">
<head>
<meta charset="utf-8">
<title>AV Glossum Business Card</title>
<link href="https://fonts.googleapis.com/css2?family=Open+Sans:wght@400;600;700&display=swap" rel="stylesheet">
<style>
  :root {
    --backdrop: #3b3b3b;
    --card: #1a1a1a;
    --card-deep: #141414;
    --brand-blue: #1e5fc0;
    --edge-blue: #2a6ad6;
    --text-light: #e6e6e6;
    --pattern-mid: #2b2b2b;
  }
  * { box-sizing: border-box; margin: 0; padding: 0; }
  html, body {
    width: 1200px; height: 801px; overflow: hidden;
    background: var(--backdrop);
    font-family: "Open Sans", Arial, sans-serif;
  }
  .stage {
    width: 1200px; height: 801px;
    display: flex; align-items: center; justify-content: center; gap: 60px;
  }
  .card {
    width: 500px; height: 286px;
    background: var(--card);
    border: 2px solid var(--edge-blue);
    position: relative; overflow: hidden;
  }
  .card-front { display: flex; align-items: center; }
  .brand-block {
    width: 230px; height: 100%;
    display: flex; align-items: center; justify-content: center;
  }
  .brand-name {
    color: var(--brand-blue); font-weight: 700; font-size: 26px; letter-spacing: 3px;
  }
  .divider {
    width: 1px; height: 200px; background: var(--brand-blue);
  }
  .contact-block {
    padding-left: 28px; color: var(--text-light); font-size: 13px; line-height: 1.5;
  }
  .person-name {
    color: var(--brand-blue); font-weight: 700; font-size: 17px; letter-spacing: 0.5px;
    text-transform: uppercase;
  }
  .person-title { font-size: 13px; margin-bottom: 12px; }
  .address { margin-bottom: 12px; }
  .contact-line { display: flex; align-items: center; gap: 8px; }
  .contact-line svg { width: 11px; height: 11px; fill: var(--brand-blue); flex: none; }
  .card-back { background: var(--card-deep); }
  .back-pattern {
    position: absolute; inset: 0;
    background: linear-gradient(135deg, #111 0%, var(--pattern-mid) 55%, #3a3a3a 100%);
  }
  .back-mark {
    position: absolute; left: 50%; top: 50%; transform: translate(-50%, -50%);
    display: flex; align-items: center; gap: 10px;
    color: var(--brand-blue); font-weight: 700; font-size: 20px; letter-spacing: 3px;
  }
  .back-mark .dot { width: 12px; height: 12px; border-radius: 50%; background: var(--brand-blue); }
</style>
</head>
<body>
<main class="stage">
  <section class="card card-front" aria-label="Business card front">
    <div class="brand-block">
      <span class="brand-name">AV GLOSSUM</span>
    </div>
    <div class="divider"></div>
    <div class="contact-block">
      <p class="person-name">Dario Venholt</p>
      <p class="person-title">President</p>
      <p class="address">4418 Harbor Crest Way<br>Bayline CA 90412</p>
      <p class="contact-line">
        <svg viewBox="0 0 24 24"><path d="M6.6 10.8a15 15 0 0 0 6.6 6.6l2.2-2.2a1 1 0 0 1 1-.25 11.4 11.4 0 0 0 3.6.6 1 1 0 0 1 1 1V20a1 1 0 0 1-1 1A17 17 0 0 1 3 4a1 1 0 0 1 1-1h3.5a1 1 0 0 1 1 1c0 1.25.2 2.45.6 3.6a1 1 0 0 1-.25 1z"/></svg>
        555-318-0427
      </p>
      <p class="contact-line">
        <svg viewBox="0 0 24 24"><path d="M2 5h20v14H2z M2 5l10 8 10-8" /></svg>
        d.venholt@avglossum.com
      </p>
      <p class="contact-line">
        <svg viewBox="0 0 24 24"><circle cx="12" cy="12" r="10"/></svg>
        www.avglossum.com
      </p>
    </div>
  </section>

  <section class="card card-back" aria-label="Business card back">
    <div class="back-pattern" role="img" aria-label="Repeating tone-on-tone brand pattern in dark greys"></div>
    <div class="back-mark"><span class="dot"></span>AV GLOSSUM</div>
  </section>
</main>
</body>
</html>
```